Bright Harbor Counseling Letterhead for hip modern business

I would like some ombre use of the colors in the logo hip letterhead that incorporates logo colors and feel, needs to connect with young professionals and college students. i need to be able to write letters to schools to excuse absences as well. i like color blocks on one side preferably using colors from the attached logo design.

Target Market(s)

high income young people, young adults and college students

Industry/Entity Type

mental health

Font styles to use
Serif
Sans Serif

Colors
0054AA
0677BA
7BADD7
CADEEF
E8F1F8
0094D4
00A9DD
6FCCEA
C7EBF8
E9F6FB
00AB8E
00BBA5
67D7C9
C6EFE9
E9F9F6
59FF00
82FF00
B8FF75
E3FFCB
F4FFEA
A7469A
B969AE
D3A5CF
EDDBEB
F8F0F9
6B429C
8869AF
B7A5CE
E3DAEB
F3F0F8

Requirements
Must have
• a modern hip feel, somewhat color

```html
<!DOCTYPE html>
<html lang="en">
<head>
<meta charset="utf-8">
<title>Bright Harbor Counseling Letterhead</title>
<link href="https://fonts.googleapis.com/css2?family=Lato:wght@300;400&display=swap" rel="stylesheet">
<style>
  :root {
    --backdrop: #2e2e2e;
    --paper: #ffffff;
    --harbor-blue: #2e74bb;
    --harbor-teal: #4fc3b5;
    --harbor-purple: #7b3595;
    --ink: #1c1c1c;
    --ink-soft: #3a3a3a;
  }
  html, body {
    margin: 0;
    padding: 0;
    width: 1200px;
    height: 1034px;
    overflow: hidden;
    background: var(--backdrop);
  }
  .letterhead {
    position: absolute;
    left: 260px;
    top: 36px;
    width: 680px;
    height: 962px;
    background: var(--paper);
    overflow: hidden;
    font-family: "Lato", sans-serif;
  }
  .header-wave {
    position: absolute;
    left: 0;
    top: 0;
    width: 680px;
    height: 260px;
  }
  .brand {
    position: absolute;
    left: 52px;
    top: 196px;
    color: var(--ink-soft);
    font-weight: 300;
    line-height: 1;
  }
  .brand-name {
    display: block;
    font-size: 27px;
    letter-spacing: 0.5px;
  }
  .brand-tagline {
    display: block;
    font-size: 13px;
    letter-spacing: 3.5px;
    margin-top: 4px;
    text-align: right;
  }
  .contact {
    position: absolute;
    right: 30px;
    bottom: 36px;
    text-align: right;
    font-size: 12.5px;
    line-height: 1.45;
    color: var(--ink);
    font-weight: 400;
  }
  .contact p { margin: 0; }
  .label-tel { color: var(--harbor-teal); }
  .label-fax { color: var(--harbor-purple); }
  .label-email { color: var(--harbor-blue); }
  .contact-web {
    color: var(--harbor-purple);
    font-size: 14px;
    letter-spacing: 0.5px;
  }
  .footer-band {
    position: absolute;
    left: 0;
    bottom: 0;
    width: 100%;
    height: 9px;
    display: flex;
  }
  .footer-band-teal { flex: 0 0 54%; background: var(--harbor-teal); }
  .footer-band-blue { flex: 1; background: var(--harbor-blue); }
</style>
</head>
<body>
  <main class="letterhead">
    <svg class="header-wave" viewBox="0 0 680 260" aria-hidden="true">
      <path d="M0 0 H680 C668 40 590 68 450 100 C300 134 120 150 40 196 C20 208 6 222 0 236 Z" fill="var(--harbor-blue)"/>
      <path d="M2 250 C50 190 190 165 340 133 C490 102 640 72 676 14" fill="none" stroke="var(--harbor-teal)" stroke-width="4"/>
      <path d="M8 262 C64 204 206 180 352 148 C506 114 650 82 680 22" fill="none" stroke="var(--harbor-purple)" stroke-width="4"/>
    </svg>

    <div class="brand">
      <span class="brand-name">Bright Harbor</span>
      <span class="brand-tagline">Counseling</span>
    </div>

    <address class="contact">
      <p>Bright Harbor Counseling</p>
      <p>Suite 410 Harbor Lane, Bayview, Zip 5810, Country</p>
      <p><span class="label-tel">Tel:</span> (00) 05550 132 470 &nbsp;<span class="label-fax">Fax:</span> (00) 05550 132 471 &nbsp;<span class="label-email">Email:</span> hello@brightharborcounseling.com</p>
      <p class="contact-web">www.brightharborcounseling.com</p>
    </address>

    <div class="footer-band">
      <div class="footer-band-teal"></div>
      <div class="footer-band-blue"></div>
    </div>
  </main>
</body>
</html>
```